Marrowick Off-Grid Energy

The company provides world wide installations and products for off-grid energy solutions. This means AC power where there is no network available. Mostly this is with solar panels combined with hybrid inverters and Lithium batteries. In the future small windmills and hydropower. The company is Dutch but has a hub in Hungary to supply the Balkan and surrounding countries.

We sell all Tovu products and also Pyramoxa and Quillbrook energy products

I have 3 versions of my logo. 2 attached and the third is the Off-grid energy text in black. Just see what works best with the design.
Obviously I need a good design but also good coding. It needs to meet al the latest (Google) search engine standards and should heave a web shop.
The web shop should be able to work with different currencies and calculate international shipping fees. Orders should be paid with; credit card, Coinwisp, Faxo or whatever is used internationally.

Coding

Coded - Design and coding required

Number of Pages Required

5+ page

Font styles to use
Other font styles liked:
• see logo

Colors
0054AA
0677BA
7BADD7
CADEEF
E8F1F8
0094D4
00A9DD
6FCCEA
C7EBF8
E9F6FB
59FF00
82FF00
B8FF75
E3FFCB
F4FFEA
EB3D1F
EC4F4E
F09395
F8D3D4
FCEDEE

Requirements
Must have
• web shop
Nice to have
• slick design
Should not have
• stupid things ;-)

```html
<!DOCTYPE html>
<html lang="en">
<head>
<meta charset="utf-8">
<title>Marrowick Off-Grid Energy</title>
<link href="https://fonts.googleapis.com/css2?family=Righteous&family=Poppins:wght@400;500;600;700&display=swap" rel="stylesheet">
<style>
:root{
  --green:#59ff00;
  --green-soft:#e3ffcb;
  --green-pale:#f4ffea;
  --red:#eb3d1f;
  --red-deep:#e0201a;
  --blue:#0054aa;
  --blue-soft:#cadeef;
  --blue-pale:#e8f1f8;
  --ink:#111;
  --text:#333;
  --muted:#666;
  --line:#ddd;
  --star:#f5a623;
  --black:#050505;
}
*{margin:0;padding:0;box-sizing:border-box}
html,body{width:1200px;height:4983px;overflow:hidden}
body{position:relative;font-family:'Poppins',sans-serif;color:var(--text);background:#fff}
.abs{position:absolute}
.heading{font-family:'Righteous',sans-serif;color:var(--ink);font-weight:400}
.center-title{position:absolute;left:0;width:1200px;text-align:center;font-size:36px}
.title-bar{position:absolute;left:565px;width:70px;height:4px;background:var(--red-deep)}
.btn{position:absolute;display:flex;align-items:center;justify-content:center;background:var(--green);color:var(--ink);font-weight:700;font-size:14px;text-transform:uppercase;clip-path:polygon(10% 0,100% 0,90% 100%,0 100%)}
.img-fill{position:absolute;border-radius:4px}

/* header */
.site-header{position:absolute;left:0;top:0;width:1200px;height:87px;background:#fff;border-top:4px solid var(--red-deep);z-index:3}
.logo{position:absolute;left:112px;top:12px;display:flex;align-items:center;gap:10px}
.logo-mark{width:26px;height:26px;background:var(--green)}
.logo-name{font-family:'Poppins',sans-serif;font-weight:600;font-size:24px;line-height:26px;color:var(--ink)}
.logo-name span{display:block;font-size:10px;line-height:14px;letter-spacing:1.5px;text-transform:uppercase}
.main-nav{position:absolute;left:367px;top:36px;display:flex;gap:26px;font-size:13px;color:#333}
.main-nav .active{color:var(--red-deep);border-bottom:2px solid var(--red-deep);font-weight:500}
.lang{position:absolute;left:938px;top:27px;width:80px;height:34px;border:1px solid #bbb;border-radius:5px;font-size:13px;font-weight:500;display:flex;align-items:center;justify-content:center;gap:6px}
.cart{position:absolute;left:1040px;top:28px}
.cart-badge{position:absolute;left:1066px;top:20px;width:20px;height:20px;border-radius:50%;background:var(--green);font-size:11px;font-weight:600;display:flex;align-items:center;justify-content:center}

/* hero */
.hero{position:absolute;left:0;top:87px;width:1200px;height:580px;overflow:hidden}
.hero-photo{position:absolute;inset:0;background:linear-gradient(180deg,#f7efe6 0%,#f2e2d0 22%,#b9c4d4 40%,#36558f 55%,#1d3a78 75%,#17306a 100%)}
.hero-title{position:absolute;top:48px;left:0;width:1200px;text-align:center;font-size:40px;line-height:50px}
.hero-sub{position:absolute;top:152px;left:0;width:1200px;text-align:center;font-size:14px;line-height:29px;color:#222}
.hero-wave{position:absolute;left:0;top:568px}

/* about */
.about-circle{position:absolute;left:165px;top:780px;width:330px;height:330px;border-radius:50%;background:#eef0f6}
.exp-badge{position:absolute;left:399px;top:1058px;width:96px;height:92px;background:var(--red-deep);color:#fff;border-radius:4px;text-align:center;font-weight:700;font-size:11px;line-height:17px;padding-top:12px}
.exp-badge b{display:block;font-size:20px;line-height:24px}
.about-title{left:623px;top:740px;font-size:36px}
.about-text{left:625px;top:820px;width:420px;font-size:12.5px;line-height:27.5px;color:#333}

/* product cards */
.card{position:absolute;background:#fff;border:1px solid #ddd;border-radius:6px;box-shadow:0 3px 8px rgba(0,0,0,.12);text-align:center}
.card-img{position:absolute;left:7px;top:7px;right:7px;height:207px;border-radius:4px}
.card h3{position:absolute;top:230px;left:0;width:100%;font-size:19px;font-weight:500;color:#111}
.card p{position:absolute;top:266px;left:20px;right:20px;font-size:12.5px;line-height:26px;color:#555}

/* services */
.services{position:absolute;left:0;top:1858px;width:1200px;height:522px;background:var(--blue-pale);clip-path:polygon(0 0,58% 12%,100% 0,100% 100%,76% 88%,0 100%)}
.services-photo{position:absolute;left:600px;top:0;width:600px;height:522px;background:linear-gradient(120deg,#d8dee5 0%,#8fa1b1 40%,#5e6c79 70%,#3a434c 100%)}
.services-fade{position:absolute;left:350px;top:0;width:450px;height:522px;background:linear-gradient(90deg,var(--blue-pale) 30%,rgba(232,241,248,0))}
.svc-title{left:110px;top:1953px;font-size:36px}
.svc-bar{position:absolute;left:112px;top:2016px;width:66px;height:4px;background:var(--red-deep)}
.svc-icon{position:absolute;width:100px;height:100px;border-radius:50%;background:var(--green);display:flex;align-items:center;justify-content:center}
.svc h3{position:absolute;font-size:19px;font-weight:600;color:#111}
.svc p{position:absolute;font-size:13px;line-height:26px;color:#444;width:310px}
.svc a{position:absolute;font-size:14px;font-weight:700;color:var(--red-deep);text-decoration:none}

/* shop */
.shop-card{position:absolute;top:2547px;height:365px;background:#fff;border:1px solid #ddd;border-radius:4px;box-shadow:0 3px 8px rgba(0,0,0,.12)}
.shop-img{position:absolute;left:20px;right:20px;top:10px;height:168px;border-radius:3px}
.shop-card h3{position:absolute;left:10px;top:195px;right:8px;font-size:19px;font-weight:600;line-height:26px;color:#111}
.stars{position:absolute;left:12px;color:var(--star);font-size:15px;letter-spacing:0}
.price{position:absolute;left:12px;font-size:15px;color:#333}
.price s{color:#888;margin-right:6px}
.shop-card .btn{width:158px;height:38px;font-size:12px;left:15px}
.slide-arrow{position:absolute;width:38px;height:38px;border-radius:50%;border:2px solid #111;background:#fff;display:flex;align-items:center;justify-content:center}
.slide-arrow.red{border-color:var(--red-deep)}

/* testimonials */
.testimonials{position:absolute;left:0;top:2970px;width:1200px;height:784px;background:linear-gradient(180deg,#c9f8a8 0%,#d8fbbd 50%,#e4fdd0 100%);clip-path:polygon(0 0,75% 7%,100% 0,100% 100%,50% 96%,0 100%)}
.quote-card{position:absolute;left:166px;top:3203px;width:852px;height:396px;background:#fff;box-shadow:0 4px 12px rgba(0,0,0,.12);text-align:center}
.quote-mark{position:absolute;left:540px;top:3152px;font-family:'Righteous',sans-serif;font-size:150px;line-height:150px;color:var(--blue)}
.avatar{position:absolute;top:3565px;width:62px;height:62px;border-radius:50%;border:3px solid #fff;box-shadow:0 2px 6px rgba(0,0,0,.2)}

/* contact */
.contact-sub{left:116px;top:3940px;font-size:24px}
.contact-item{position:absolute;left:112px;display:flex;gap:14px}
.contact-icon{width:48px;height:48px;border-radius:50%;background:var(--green);display:flex;align-items:center;justify-content:center;flex:none}
.contact-item small{display:block;font-size:12px;font-weight:600;color:#111;margin-top:2px}
.contact-item span{font-size:17px;font-weight:500;color:#111;line-height:28px}
.form-frame{position:absolute;left:608px;top:4305px;width:462px;height:160px;background:var(--red-deep)}
.form-box{position:absolute;left:625px;top:3889px;width:430px;height:542px;background:#fff;border:1px solid #e3e3e3;box-shadow:0 2px 10px rgba(0,0,0,.1)}
.form-box h3{position:absolute;left:30px;top:26px;font-size:19px;font-weight:500;color:#222}
.field{position:absolute;left:33px;width:370px;border-bottom:1px solid #bbb;height:56px}
.field label{display:block;font-size:13px;font-weight:600;color:#222}
.field span{display:block;font-size:12.5px;color:#444;margin-top:4px}
.field svg{position:absolute;right:4px;top:12px}

/* footer */
.site-footer{position:absolute;left:0;top:4528px;width:1200px;height:455px;background:var(--black)}
.footer-logo{position:absolute;left:122px;top:4700px;display:flex;align-items:center;gap:10px;color:#fff}
.footer-logo .logo-name{color:#fff}
.socials{position:absolute;left:140px;top:4826px;display:flex;gap:14px}
.social{display:flex;align-items:center;gap:4px;color:#fff;font-size:10px}
.social i{width:12px;height:12px;border-radius:50%;background:#fff;display:block}
.foot-col{position:absolute;top:4656px;color:#fff}
.foot-col h4{font-size:18px;font-weight:500;text-transform:uppercase;margin-bottom:12px}
.foot-col li{list-style:none;font-size:14px;line-height:34px;display:flex;align-items:center;gap:10px}
.foot-divider{position:absolute;left:110px;top:4904px;width:980px;height:1px;background:#777}
.copyright{position:absolute;left:110px;top:4938px;color:#fff;font-size:12.5px}
.payments{position:absolute;left:660px;top:4937px;display:flex;gap:6px}
.payments span{width:34px;height:20px;background:#f2f2f2;border-radius:3px;font-size:7px;color:#222;display:flex;align-items:center;justify-content:center;font-weight:600}
</style>
</head>
<body>

<header class="site-header">
  <div class="logo">
    <div class="logo-mark"></div>
    <div class="logo-name">Marrowick<span>Off-Grid Energy</span></div>
  </div>
  <nav class="main-nav">
    <span class="active">HOME</span><span>ABOUT US</span><span>SHOP</span><span>SERVICES</span><span>PRODUCTS</span><span>CONTACT US</span>
  </nav>
  <div class="lang">ENG
    <svg width="12" height="8" viewBox="0 0 12 8"><path d="M1 1l5 5 5-5" fill="none" stroke="#111" stroke-width="2"/></svg>
  </div>
  <svg class="cart" width="34" height="30" viewBox="0 0 34 30"><path d="M1 3h5l4 17h18l4-12H9" fill="none" stroke="#111" stroke-width="2.4" stroke-linejoin="round"/><circle cx="12" cy="26" r="2.5" fill="#111"/><circle cx="26" cy="26" r="2.5" fill="#111"/></svg>
  <div class="cart-badge">0</div>
</header>

<section class="hero">
  <div class="hero-photo" role="img" aria-label="Solar panel field under a sunset sky"></div>
  <h1 class="hero-title heading">Energy Independence with Solar, Wind,<br>and Battery Storage</h1>
  <p class="hero-sub">Lorem Ipsum is simply dummy text of the printing and<br>typesetting industry.</p>
  <div class="btn" style="left:502px;top:223px;width:192px;height:50px">Get Started</div>
</section>
<svg class="hero-wave" width="1200" height="100" viewBox="0 0 1200 100" style="top:580px">
  <path d="M0 60 Q300 35 600 20 Q900 35 1200 45 L1200 100 L0 100Z" fill="var(--green)"/>
  <path d="M0 72 Q300 52 600 42 Q900 52 1200 62 L1200 100 L0 100Z" fill="#fff"/>
</svg>

<!-- about -->
<div class="about-circle"></div>
<div class="img-fill" style="left:207px;top:724px;width:165px;height:178px;background:linear-gradient(180deg,#9cc3e8 0%,#5b7fae 55%,#6d8a4a 100%)" role="img" aria-label="House with rooftop solar panels and a small wind turbine"></div>
<div class="img-fill" style="left:393px;top:803px;width:180px;height:234px;background:linear-gradient(180deg,#8fb8e0 0%,#2f4f8a 50%,#5f8c3a 100%)" role="img" aria-label="Ground mounted solar panels on grass"></div>
<div class="img-fill" style="left:120px;top:921px;width:257px;height:267px;background:linear-gradient(180deg,#2d4f8f 0%,#5a7bb0 45%,#e8e8e8 70%,#cfd3d8 100%)" role="img" aria-label="Solar panels with inverter and battery units on a wall"></div>
<div class="exp-badge"><b>20+</b>YEARS OF<br>EXPERIENCE</div>
<h2 class="abs heading about-title">About Us</h2>
<p class="abs about-text">Lorem Ipsum is simply dummy text of the printing and typesetting industry. Lorem Ipsum has been the industry's standard dummy text ever since the 1500s, when an unknown printer took a galley of type and scrambled it to make a type specimen book.<br>It has survived not only five centuries, but also the leap into electronic typesetting, remaining essentially unchanged. Lorem Ipsum is simply dummy text of the printing and typesetting industry. Lorem Ipsum has been the industry's standard dummy text ever since the 1500s,</p>
<div class="btn" style="left:625px;top:1117px;width:196px;height:50px">Read More</div>

<!-- products we sell -->
<h2 class="heading center-title" style="top:1258px">Products We Sell</h2>
<div class="title-bar" style="top:1323px"></div>
<div class="card" style="left:110px;top:1364px;width:308px;height:347px">
  <div class="card-img" style="background:linear-gradient(180deg,#6fa5dd 0%,#2b4f91 45%,#16316a 100%)" role="img" aria-label="Solar panels under a blue sky"></div>
  <h3>Solar Panels</h3><p>Lorem Ipsum is simply dummy text of the printing and typesetting</p>
</div>
<div class="card" style="left:447px;top:1364px;width:308px;height:347px">
  <div class="card-img" style="background:linear-gradient(90deg,#dfe3e6 0%,#f4f5f6 40%,#9aa5ad 75%,#6f7b58 100%)" role="img" aria-label="Hybrid inverter mounted on a house wall"></div>
  <h3>Hybrid Inverters</h3><p>Lorem Ipsum is simply dummy text of the printing and typesetting</p>
</div>
<div class="card" style="left:784px;top:1364px;width:308px;height:347px">
  <div class="card-img" style="background:linear-gradient(180deg,#4a4d52 0%,#c9cdd1 50%,#8a8f96 100%)" role="img" aria-label="Lithium battery cells on a production line"></div>
  <h3>Lithium batteries</h3><p>Lorem Ipsum is simply dummy text of the printing and typesetting</p>
</div>
<div class="btn" style="left:502px;top:1746px;width:196px;height:50px">View More</div>

<!-- services -->
<section class="services">
  <div class="services-photo" role="img" aria-label="Close view of a wall mounted inverter"></div>
  <div class="services-fade"></div>
</section>
<h2 class="abs heading svc-title">Our Services</h2>
<div class="svc-bar"></div>
<div class="svc">
  <div class="svc-icon" style="left:112px;top:2047px">
    <svg width="52" height="52" viewBox="0 0 52 52" fill="none" stroke="#111" stroke-width="3" stroke-linecap="round"><path d="M10 42L34 18M30 12a8 8 0 0 0 10 10M12 10l30 32M8 14l6-6"/></svg>
  </div>
  <h3 style="left:235px;top:2048px">Professional Installation Services</h3>
  <p style="left:239px;top:2080px">Lorem Ipsum is simply dummy text of the printing and typesetting industry.</p>
  <a style="left:239px;top:2137px">READ MORE</a>
</div>
<div class="svc">
  <div class="svc-icon" style="left:112px;top:2180px">
    <svg width="52" height="52" viewBox="0 0 52 52" fill="none" stroke="#111" stroke-width="3" stroke-linejoin="round"><path d="M8 18h22v16H8zM30 24h8l6 6v4H30z"/><circle cx="15" cy="38" r="4"/><circle cx="36" cy="38" r="4"/></svg>
  </div>
  <h3 style="left:239px;top:2180px">Worldwide Shipping &amp; Support</h3>
  <p style="left:242px;top:2212px">Lorem Ipsum is simply dummy text of the printing and typesetting industry.</p>
  <a style="left:242px;top:2269px">READ MORE</a>
</div>

<!-- best selling -->
<h2 class="heading center-title" style="top:2428px">Best Selling Products</h2>
<div class="title-bar" style="top:2494px"></div>
<div class="slide-arrow" style="left:31px;top:2713px"><svg width="14" height="14" viewBox="0 0 14 14"><path d="M9 2L4 7l5 5" fill="none" stroke="#111" stroke-width="2"/></svg></div>
<div class="slide-arrow red" style="left:1123px;top:2713px"><svg width="14" height="14" viewBox="0 0 14 14"><path d="M5 2l5 5-5 5" fill="none" stroke="#e0201a" stroke-width="2"/></svg></div>

<div class="shop-card" style="left:110px;width:236px">
  <div class="shop-img" style="left:55px;right:55px;background:linear-gradient(160deg,#2a3a5a,#111a2e)" role="img" aria-label="Solar panel product"></div>
  <h3 style="top:202px">Tovu Solar Panels</h3>
  <div class="stars" style="top:240px">★★★★★</div>
  <div class="price" style="top:264px"><s>$93.88</s>$54.49</div>
  <div class="btn" style="top:310px">Add to cart</div>
</div>
<div class="shop-card" style="left:360px;width:233px">
  <div class="shop-img" style="left:50px;right:50px;background:linear-gradient(160deg,#f4f5f6,#c5cacf)" role="img" aria-label="Off-grid inverter product"></div>
  <h3>Pyramoxa off-grid inverters</h3>
  <div class="stars" style="top:248px">★★★★★</div>
  <div class="price" style="top:272px"><s>$93.88</s>$54.49</div>
  <div class="btn" style="top:310px">Add to cart</div>
</div>
<div class="shop-card" style="left:606px;width:234px">
  <div class="shop-img" style="left:0;right:0;top:20px;height:140px;background:linear-gradient(180deg,#5c5f63,#1e1f22)" role="img" aria-label="Lithium battery pack product"></div>
  <h3>Pyramoxa Lithium batteries</h3>
  <div class="stars" style="top:248px">★★★★★</div>
  <div class="price" style="top:272px"><s>$93.88</s>$54.49</div>
  <div class="btn" style="top:310px">Add to cart</div>
</div>
<div class="shop-card" style="left:853px;width:237px">
  <div class="shop-img" style="left:50px;right:50px;background:linear-gradient(160deg,#2a3a5a,#111a2e)" role="img" aria-label="Solar panel product"></div>
  <h3>Quillbrook energy Solar Panels</h3>
  <div class="stars" style="top:248px">★★★★★</div>
  <div class="price" style="top:272px"><s>$93.88</s>$54.49</div>
  <div class="btn" style="top:310px">Add to cart</div>
</div>

<!-- testimonials -->
<section class="testimonials" role="img" aria-label="Faded house with solar roof behind a green tint"></section>
<h2 class="heading center-title" style="top:3072px">Our Testimonials</h2>
<div class="quote-card">
  <h3 style="position:absolute;top:58px;width:100%;font-size:19px;font-weight:600;color:#111">Lorem Ipsum is simply dummy text</h3>
  <p style="position:absolute;top:120px;left:90px;right:90px;font-size:13.5px;line-height:31px;color:#333">Lorem Ipsum is simply dummy text of the printing and typesetting industry. Lorem Ipsum has been the industry's standard dummy text ever since the 1500s<br>Lorem Ipsum is simply dummy text of the printing and typesetting industry. Lorem Ipsum</p>
  <div style="position:absolute;top:236px;width:100%;color:var(--star);font-size:22px">★★★★★</div>
  <div style="position:absolute;top:276px;width:100%;color:var(--red-deep);font-size:19px;font-weight:600">Ravel</div>
  <div style="position:absolute;top:312px;width:100%;font-size:13px;color:#333">Client</div>
  <div style="position:absolute;top:336px;left:406px;display:flex;gap:8px"><i style="width:6px;height:6px;border-radius:50%;background:var(--blue)"></i><i style="width:6px;height:6px;border-radius:50%;background:#ccc"></i><i style="width:6px;height:6px;border-radius:50%;background:#ccc"></i><i style="width:6px;height:6px;border-radius:50%;background:#ccc"></i></div>
</div>
<div class="quote-mark">“</div>
<div class="slide-arrow" style="left:147px;top:3380px"><svg width="14" height="14" viewBox="0 0 14 14"><path d="M9 2L4 7l5 5" fill="none" stroke="#111" stroke-width="2"/></svg></div>
<div class="slide-arrow red" style="left:1007px;top:3380px"><svg width="14" height="14" viewBox="0 0 14 14"><path d="M5 2l5 5-5 5" fill="none" stroke="#e0201a" stroke-width="2"/></svg></div>
<div class="avatar" style="left:478px;background:#c4cdd6" role="img" aria-label="Client portrait"></div>
<div class="avatar" style="left:557px;top:3558px;width:76px;height:76px;background:#f2a23c" role="img" aria-label="Client portrait, selected"></div>
<div class="avatar" style="left:650px;background:#c4cdd6" role="img" aria-label="Client portrait"></div>

<!-- contact -->
<h2 class="heading center-title" style="top:3780px">Contact Us</h2>
<div class="title-bar" style="top:3846px"></div>
<h3 class="abs heading contact-sub">Feel Free To Contact Us</h3>
<div class="contact-item" style="top:4010px">
  <div class="contact-icon"><svg width="24" height="24" viewBox="0 0 24 24"><path d="M5 3h4l2 5-3 2a12 12 0 0 0 6 6l2-3 5 2v4a2 2 0 0 1-2 2A18 18 0 0 1 3 5a2 2 0 0 1 2-2z" fill="none" stroke="#111" stroke-width="2"/></svg></div>
  <div><small>CALL US</small><span>+1 555 010 2040</span></div>
</div>
<div class="contact-item" style="top:4102px">
  <div class="contact-icon"><svg width="24" height="24" viewBox="0 0 24 24" fill="none" stroke="#111" stroke-width="2"><rect x="3" y="5" width="18" height="14"/><path d="M3 5l9 8 9-8"/></svg></div>
  <div><small>MAIL US</small><span>info@marrowick.com</span></div>
</div>
<div class="contact-item" style="top:4194px">
  <div class="contact-icon"><svg width="24" height="24" viewBox="0 0 24 24" fill="none" stroke="#111" stroke-width="2"><path d="M12 22s7-7 7-12a7 7 0 0 0-14 0c0 5 7 12 7 12z"/><circle cx="12" cy="10" r="2.5"/></svg></div>
  <div><small>OUR LOCATION</small><span>303, Lorem Ipsum is simply<br>dummy text of the printing</span></div>
</div>

<div class="form-frame"></div>
<div class="form-box">
  <h3>Send Us A Message</h3>
  <div class="field" style="top:70px"><label>Name</label><span>Tomas Brennick</span>
    <svg width="22" height="22" viewBox="0 0 22 22" fill="none" stroke="#777" stroke-width="1.5"><circle cx="11" cy="7" r="4"/><path d="M3 20c1-5 15-5 16 0z"/></svg></div>
  <div class="field" style="top:138px"><label>Email Address</label><span>tomas.brennick@postvale.net</span>
    <svg width="24" height="20" viewBox="0 0 24 20" fill="none" stroke="#777" stroke-width="1.5"><rect x="2" y="3" width="20" height="14"/><path d="M2 3l10 8 10-8"/></svg></div>
  <div class="field" style="top:206px"><label>Address</label><span>13, Lorem Ipsum, CA</span>
    <svg width="22" height="24" viewBox="0 0 22 24" fill="none" stroke="#777" stroke-width="1.5"><path d="M11 20s6-6 6-10a6 6 0 0 0-12 0c0 4 6 10 6 10z"/><circle cx="11" cy="10" r="2"/></svg></div>
  <div class="field" style="top:280px"><label>Subject</label><span>Typer Here</span>
    <svg width="20" height="24" viewBox="0 0 20 24" fill="none" stroke="#777" stroke-width="1.5"><rect x="3" y="2" width="14" height="20"/><path d="M6 18h8"/></svg></div>
  <div class="field" style="top:350px;height:96px"><label>Message</label>
    <svg width="22" height="22" viewBox="0 0 22 22" fill="none" stroke="#777" stroke-width="1.5"><path d="M4 14a8 7 0 1 1 3 4l-4 2 1-6z"/></svg></div>
  <div class="btn" style="left:205px;top:477px;width:205px;height:46px">Send Message</div>
</div>

<!-- footer -->
<svg class="abs" style="left:0;top:4510px" width="1200" height="90" viewBox="0 0 1200 90">
  <path d="M0 18 Q600 70 1200 18 L1200 90 L0 90Z" fill="var(--green)"/>
  <path d="M0 30 Q600 82 1200 30 L1200 90 L0 90Z" fill="var(--black)"/>
</svg>
<footer class="site-footer" style="top:4550px;height:433px">
</footer>
<div class="footer-logo">
  <div class="logo-mark"></div>
  <div class="logo-name">Marrowick<span>Off-Grid Energy</span></div>
</div>
<div class="socials">
  <span class="social"><i></i>Chirpo</span><span class="social"><i></i>Pixa</span><span class="social"><i></i>Snaply</span><span class="social"><i></i>Tokko</span>
</div>
<div class="foot-col" style="left:428px">
  <h4>Quick Links</h4>
  <ul><li>➜ Home</li><li>➜ About Us</li><li>➜ Shop</li><li>➜ Services</li><li>➜ Products</li></ul>
</div>
<div class="foot-col" style="left:660px">
  <h4>Help Links</h4>
  <ul><li>➜ FAQ</li><li>➜ Terms of use</li><li>➜ Privacy Policy</li><li>➜ Support Links</li><li>➜ Conditions</li></ul>
</div>
<div class="foot-col" style="left:873px">
  <h4>Contact Us</h4>
  <ul>
    <li style="align-items:flex-start;line-height:28px"><svg width="28" height="28" viewBox="0 0 24 24"><circle cx="12" cy="12" r="12" fill="#fff"/><path d="M12 19s5-5 5-9a5 5 0 0 0-10 0c0 4 5 9 5 9z" fill="#111"/></svg><span>Marrowick<br>Hungary</span></li>
    <li style="margin-top:8px"><svg width="28" height="28" viewBox="0 0 24 24"><circle cx="12" cy="12" r="12" fill="#fff"/><path d="M8 6h2l1 3-2 1a7 7 0 0 0 4 4l1-2 3 1v2a1 1 0 0 1-1 1A10 10 0 0 1 7 7a1 1 0 0 1 1-1z" fill="#111"/></svg>+1 555 010 2040</li>
    <li style="margin-top:8px"><svg width="28" height="28" viewBox="0 0 24 24"><circle cx="12" cy="12" r="12" fill="#fff"/><rect x="6" y="8" width="12" height="9" fill="none" stroke="#111" stroke-width="1.6"/><path d="M6 8l6 5 6-5" fill="none" stroke="#111" stroke-width="1.6"/></svg>info@marrowick.com</li>
  </ul>
</div>
<div class="foot-divider"></div>
<div class="copyright">Copyrights@2025. Marrowick .All Rights Reserved</div>
<div class="payments">
  <span>Strovo</span><span>Amvero</span><span>Pomely</span><span>Dixo</span><span>Goopa</span><span>Mirocard</span><span>Coinwisp</span><span>Faxo</span><span>Venla</span><span>Vexa</span><span>Kloro</span>
</div>

</body>
</html>
```